flyer for a contemporary music concert: GILDED TALL HORN HAZE

We are an ensemble of contemporary music turning 10 years in 2019. Our next concert is a cooperation with the northernmost chamber orchestra, the fjordvik consortia. Our program is with live electronic, video and a big setup (like bigband). We would like to have a flyer promoting this event.- The speciality is contemporary on the on the one hand but this particulary program is quite popular with the big setup, the brass, the electronics and video - it aims for a club-audience more than the "normal" classical music audience.

Target Market(s)

young audience interested in going to concerts, club generation 20-30 years

Font styles to use
Serif
Sans Serif

Colors

Designer to choose colors to be used in the design.

Requirements
Must have
• feeling of contemporary art, we are playing classical music but pieces of composers that are still alive - design should transport this.
• here is the link to the concertplace:
• https://www.kornwiese.org/de/event/gilded-tall-horn-haze/
• here is the link to the ensemble:
• www.lagatosombria.de
• format: "DIN lang" (105mm x 210mm)
• two pages: front and backsinde.
Nice to have
• could be crazy, not too classical
• you could use the attached images, but no need at all! Important are just the two logos of the ensembles (logo1, logo2) and the logos of the funding partners (logo3, logo4)
Should not have
• - no clipart, musical symbols like notes, key symbols or something like this you would expect in a poster for a music school advertising
• - no hand writing font

```html
<!DOCTYPE html>
<html lang="de">
<head>
<meta charset="utf-8">
<title>Gilded Tall Horn Haze – Flyer DIN lang</title>
<link rel="stylesheet" href="https://fonts.googleapis.com/css2?family=Playfair+Display:wght@400;700;900&family=Montserrat:wght@400;500;600;700&display=swap">
<style>
  :root {
    --neon: #00ff66;
    --white: #ffffff;
    --ink: #141414;
    --amber: #8a5a1e;
    --umber: #4a2c12;
    --night: #1a0e07;
    --badge: #cfcfcf;
    --serif: "Playfair Display", Georgia, serif;
    --sans: "Montserrat", Arial, sans-serif;
  }
  * { box-sizing: border-box; margin: 0; padding: 0; }
  html, body { width: 1200px; height: 1000px; overflow: hidden; background: var(--white); }
  .sheet { position: relative; width: 1200px; height: 1000px; }

  .page {
    position: absolute; top: 50px; width: 450px; height: 900px; overflow: hidden;
    color: var(--white); text-align: center;
  }
  .page--front { left: 135px; }
  .page--back { left: 615px; }

  .page__backdrop { position: absolute; inset: 0; }
  .page--front .page__backdrop {
    background: linear-gradient(180deg, var(--amber) 0%, #7a4e1a 30%, var(--umber) 60%, #2a1a0e 100%);
  }
  .page--back .page__backdrop {
    background: linear-gradient(180deg, #3a1e0c 0%, #5a3416 30%, #3b200e 55%, var(--night) 100%);
  }

  .masthead { position: relative; }
  .masthead__kicker {
    font-family: var(--serif); font-weight: 400; font-size: 30px;
    letter-spacing: 18px; padding-left: 18px; line-height: 1;
  }
  .masthead__hero {
    font-family: var(--serif); font-weight: 900; color: var(--neon);
    font-size: 150px; letter-spacing: -5px; line-height: 0.9; margin-top: 4px;
  }
  .masthead__line {
    font-family: var(--serif); font-weight: 700; font-size: 44px;
    letter-spacing: 7px; line-height: 1; margin-top: 8px;
  }
  .masthead__partners {
    font-family: var(--sans); font-weight: 600; color: var(--neon);
    font-size: 10px; letter-spacing: 2.4px; margin-top: 12px;
  }
  .page--front .masthead { padding-top: 82px; }
  .page--back .masthead { padding-top: 96px; }
  .page--back .masthead__hero { font-size: 162px; }
  .page--back .masthead__line { font-size: 46px; }

  .feature {
    position: relative; display: block; width: 308px; margin: 30px auto 0;
    background: var(--white); color: var(--ink);
    font-family: var(--sans); font-weight: 700; font-size: 13px;
    letter-spacing: -0.3px; padding: 3px 0;
  }

  .programme { position: relative; width: 343px; margin: 14px auto 0; list-style: none; }
  .programme__item {
    font-family: var(--sans); padding: 9px 0 12px;
    border-bottom: 1.5px solid var(--neon);
  }
  .programme__item:last-child { border-bottom: none; }
  .programme__composer { font-weight: 700; font-size: 14px; display: block; }
  .programme__work { font-weight: 400; font-size: 14px; display: block; margin-top: 3px; }
  .programme__meta { font-size: 10px; }
  .programme__note { font-size: 11px; display: block; margin-top: 4px; }

  .ensemble-photo {
    position: absolute; left: 0; right: 0; bottom: 0; height: 170px;
    background: linear-gradient(180deg, rgba(30,20,14,0) 0%, #1d1511 45%, #2c2a2a 100%);
  }

  .about {
    position: absolute; left: 31px; right: 31px; top: 448px;
    font-family: var(--sans); font-weight: 500; font-size: 13.2px; line-height: 1.62;
    text-align: justify;
  }
  .about p + p { margin-top: 18px; }
  .about strong { font-weight: 700; }

  .sponsors { position: absolute; left: 31px; top: 744px; width: 378px; height: 104px; }
  .sponsors__badge, .sponsors__ensemble { position: absolute; background: var(--white); }
  .sponsors__badge--city { left: 0; top: 0; width: 157px; height: 54px; }
  .sponsors__badge--state { left: 167px; top: 0; width: 90px; height: 54px; }
  .sponsors__badge--city::after, .sponsors__badge--state::after {
    content: ""; position: absolute; inset: 10px 14px; background: var(--badge);
  }
  .sponsors__ensemble {
    display: flex; align-items: center; justify-content: center; gap: 8px;
    color: var(--ink);
  }
  .sponsors__ensemble--home {
    left: 0; top: 60px; width: 257px; height: 44px;
    font-family: var(--sans); font-weight: 700; font-size: 20px; letter-spacing: -0.8px;
  }
  .sponsors__ensemble--home .sponsors__mark { width: 18px; height: 18px; background: var(--ink); }
  .sponsors__ensemble--guest {
    left: 264px; top: 0; width: 114px; height: 104px; padding-top: 40px;
    font-family: var(--serif); font-weight: 400; font-size: 9px; letter-spacing: 0.3px;
  }
</style>
</head>
<body>
<main class="sheet">

  <section class="page page--front" aria-label="Vorderseite">
    <div class="page__backdrop" role="img" aria-label="Warm braun-goldene Textur mit Konzertstimmung"></div>
    <header class="masthead">
      <p class="masthead__kicker">GILDED</p>
      <h1 class="masthead__hero">TALL</h1>
      <p class="masthead__line">HORN HAZE</p>
      <p class="masthead__partners">LA GATO SOMBRIA UND FJORDVIK CONSORTIA</p>
    </header>
    <span class="feature">FEATURING&nbsp; RUNA VESTLI HARKMO</span>
    <ul class="programme">
      <li class="programme__item">
        <span class="programme__composer">EIVIND STRANDMO</span>
        <span class="programme__work">MESSINGKONZERT</span>
        <span class="programme__note">(2019 UA) 14' DER KOMPONIST IST ANWESEND.</span>
      </li>
      <li class="programme__item">
        <span class="programme__composer">KONRAD LEITH</span>
        <span class="programme__work">CIRCUITS FOR STATIC <span class="programme__meta">(2015) 16'</span></span>
      </li>
      <li class="programme__item">
        <span class="programme__composer">LORENZ GADNER</span>
        <span class="programme__work">SEVEN KNOTS FOR TEN <span class="programme__meta">(2013) 11'</span></span>
      </li>
      <li class="programme__item">
        <span class="programme__composer">DANIEL MARSH</span>
        <span class="programme__work">NEON OVER WATER <span class="programme__meta">(2001) 7'</span></span>
      </li>
      <li class="programme__item">
        <span class="programme__composer">HALLGRÍMUR ROSENTHAL:</span>
        <span class="programme__work">POLAR DRIFT <span class="programme__meta">(2017) 12'</span></span>
      </li>
    </ul>
    <div class="ensemble-photo" role="img" aria-label="Foto: Ensemble als Silhouetten in einer Winterlandschaft"></div>
  </section>

  <section class="page page--back" aria-label="Rückseite">
    <div class="page__backdrop" role="img" aria-label="Dunkle, warm braune Textur mit unscharfem Bühnenlicht"></div>
    <header class="masthead">
      <p class="masthead__kicker">GILDED</p>
      <h2 class="masthead__hero">TALL</h2>
      <p class="masthead__line">HORN HAZE</p>
      <p class="masthead__partners">LA GATO SOMBRIA UND FJORDVIK CONSORTIA</p>
    </header>
    <div class="about">
      <p><strong>In dem gemeinsamen</strong> Konzertprojekt Gilded Tall Horn Haze präsentiert das Ensemble für aktuelle Musik La Gato Sombria aus Halvmark gemeinsam mit einem Kammerorchester aus dem hohen Norden, der Fjordvik Consortia aus Nordvik.</p>
      <p>Zum 10-jährigen Jubiläum des Halvmarker Ensembles beschenkt es damit die Hörer*innen und sich selbst gleichermaßen, indem es weiter das tut, was es am besten kann: Partnerschaften eingehen, Teilnahme ermöglichen, Grenzen zu überschreiten – klassische Musik, knarzige Avantgarde, furiose Jazz- und groovige Rocksounds, dazu Live Elektronik und Filminstallationen.</p>
    </div>
    <div class="sponsors">
      <div class="sponsors__badge sponsors__badge--city" aria-label="Förderpartner"></div>
      <div class="sponsors__badge sponsors__badge--state" aria-label="Förderpartner"></div>
      <div class="sponsors__ensemble sponsors__ensemble--home"><span class="sponsors__mark"></span>la gato sombria</div>
      <div class="sponsors__ensemble sponsors__ensemble--guest">FJORDVIK CONSORTIA</div>
    </div>
  </section>

</main>
</body>
</html>
```